Business Card Design

We need a business card design for an existing business. Our main trading brand is www.brightmeadowsaver.co.uk

We attach various logo files - please use the version that will produce the sharpest image on the business card.

We are flexible about shape of card etc. Please think outside the box as to what goes on front and what goes on back of the card

We want to be able to amend the card (once the design has been agreed ) to add additional staff details, but the text to go on it will be generic

Details to go on card ( for the first generic one) are fairly minimal as we don't like cluttered business cards:-

Tom Harker
Managing Director

Mobile: 07812 548 207
Email: t.harker@brightmeadowsaver.co.uk

```html
<!DOCTYPE html>
<html lang="en">
<head>
<meta charset="utf-8">
<title>Bright Meadow Saver – Business Card</title>
<link rel="stylesheet" href="https://fonts.googleapis.com/css2?family=Exo+2:wght@400;500;600&display=swap">
<style>
  :root {
    --backdrop: #8f9193;
    --card: #ffffff;
    --brand-navy: #365d7d;
    --brand-ink: #2d4f6b;
    --brand-accent: #4fa3d9;
    --text-light: #ffffff;
    --shadow: rgba(0,0,0,0.28);
  }
  * { box-sizing: border-box; margin: 0; padding: 0; }
  html, body {
    width: 1200px; height: 771px; overflow: hidden;
    background: var(--backdrop);
    font-family: "Exo 2", "Trebuchet MS", sans-serif;
  }
  .canvas {
    position: relative; width: 1200px; height: 771px;
    display: flex; align-items: center; justify-content: center; gap: 50px;
  }
  .card {
    position: relative; width: 525px; height: 300px;
    background: var(--card);
    box-shadow: 0 10px 28px var(--shadow);
    overflow: hidden;
  }
  .card-art { position: absolute; inset: 0; }
  .contact-block {
    position: absolute; left: 30px; top: 30px;
    color: var(--text-light);
  }
  .person-name {
    font-size: 21px; font-weight: 600; letter-spacing: 2px;
    text-transform: uppercase;
  }
  .person-role { font-size: 13px; margin-top: 2px; letter-spacing: 0.5px; }
  .address { font-size: 12.5px; line-height: 1.45; margin-top: 20px; letter-spacing: 0.5px; }
  .contact-list { list-style: none; margin-top: 18px; }
  .contact-list li {
    display: flex; align-items: center; gap: 8px;
    font-size: 12px; line-height: 1; margin-bottom: 8px; letter-spacing: 0.4px;
  }
  .contact-list svg { width: 12px; height: 12px; flex: none; }
  .wordmark {
    display: flex; align-items: center; gap: 6px;
    color: var(--brand-ink); font-weight: 500; letter-spacing: 0.2px;
    white-space: nowrap;
  }
  .wordmark-dot { background: var(--brand-accent); border-radius: 50%; flex: none; }
  .card-front .wordmark {
    position: absolute; right: 16px; top: 172px; font-size: 13px;
  }
  .card-front .wordmark-dot { width: 11px; height: 11px; }
  .card-back { display: flex; align-items: center; justify-content: center; }
  .card-back .wordmark { font-size: 30px; }
</style>
</head>
<body>
<main class="canvas">

  <section class="card card-front" aria-label="Card front">
    <svg class="card-art" viewBox="0 0 525 300" aria-hidden="true">
      <path d="M0 0 H345 C292 85 270 195 282 300 H0 Z" fill="var(--brand-navy)"/>
      <path d="M366 0 C312 85 290 195 300 300 H293 C282 195 304 85 358 0 Z" fill="var(--brand-navy)"/>
    </svg>

    <div class="contact-block">
      <h1 class="person-name">Tom Harker</h1>
      <p class="person-role">Managing Director</p>
      <p class="address">14 Harbour Court,<br>Mill Lane LK2</p>
      <ul class="contact-list">
        <li>
          <svg viewBox="0 0 12 12"><path d="M2.5 1 L4.5 1 L5.3 3.4 L4 4.4 C4.6 5.8 6.2 7.4 7.6 8 L8.6 6.7 L11 7.5 L11 9.5 C11 10.3 10.3 11 9.5 11 C5 11 1 7 1 2.5 C1 1.7 1.7 1 2.5 1 Z" fill="none" stroke="#fff" stroke-width="1"/></svg>
          07812 548 207
        </li>
        <li>
          <svg viewBox="0 0 12 12"><rect x="1.5" y="3" width="9" height="7" rx="1" fill="#fff"/><rect x="3.5" y="1" width="5" height="3" fill="#fff"/></svg>
          01632 960 418
        </li>
        <li>
          <svg viewBox="0 0 12 12"><rect x="1" y="2.5" width="10" height="7" fill="#fff"/><path d="M1 2.5 L6 6.5 L11 2.5" fill="none" stroke="var(--brand-navy)" stroke-width="1"/></svg>
          t.harker@brightmeadowsaver.co.uk
        </li>
        <li>
          <svg viewBox="0 0 12 12"><circle cx="6" cy="6" r="5" fill="none" stroke="#fff"/><ellipse cx="6" cy="6" rx="2.2" ry="5" fill="none" stroke="#fff"/><path d="M1 6 H11" stroke="#fff"/></svg>
          www.brightmeadowsaver.co.uk
        </li>
      </ul>
    </div>

    <div class="wordmark">
      <span>brightmeadowsaver.co.uk</span>
      <span class="wordmark-dot"></span>
    </div>
  </section>

  <section class="card card-back" aria-label="Card back">
    <div class="wordmark">
      <span>brightmeadowsaver.co.uk</span>
    </div>
  </section>

</main>
</body>
</html>
```